Ironbark Shift Workforce

We are a underground coal mining labour hire company, needing a website that links into our online payroll (www.wagetrackly.com.au) and also need to have job applications page that is a preform with drop down menu,s with answers or check boxes. We would also need a 3 tier administration access for access to different files.
We are looking for an ongoing relationship with future app integration

Reason: There are a few more designs to come and I'm out at the mine for another week

Industry/Entity Type

Coal Mining

```html
<!DOCTYPE html>
<html lang="en">
<head>
<meta charset="utf-8">
<title>Ironbark Shift Workforce</title>
<link rel="stylesheet" href="https://fonts.googleapis.com/css2?family=Maven+Pro:wght@400;500;700&family=Tinos:ital,wght@0,400;1,700&display=swap">
<style>
:root{
  --orange:#f7931e;
  --orange-soft:#fde9d6;
  --black:#000;
  --grey-bar:#8c8c8c;
  --grey-side:#cccccc;
  --grey-light:#f3f3f3;
  --grey-head:#e3e3e3;
  --text:#222;
  --quote:#8a8a8a;
  --white:#fff;
}
*{margin:0;padding:0;box-sizing:border-box}
html,body{width:1200px;height:1000px;overflow:hidden;background:var(--white)}
body{position:relative;font-family:"Maven Pro",Arial,sans-serif;color:var(--text)}
.abs{position:absolute}
.topbar{left:334px;top:36px;width:547px;height:22px;background:var(--grey-bar);color:var(--white);font-size:8px}
.topbar .contact{position:absolute;left:76px;top:7px;display:flex;gap:12px;align-items:center}
.topbar .contact span{display:flex;gap:4px;align-items:center}
.topbar .social{position:absolute;right:69px;top:4px;display:flex;gap:3px}
.dot{width:13px;height:13px;border-radius:50%;background:#bdbdbd}
.rule{left:334px;width:547px;background:var(--orange)}
.header{left:334px;top:61px;width:547px;height:60px;background:var(--grey-light)}
.brand{position:absolute;left:70px;top:3px;display:flex;align-items:center;gap:8px}
.brand-mark{width:50px;height:50px;border-radius:50%;border:3px solid var(--orange);background:var(--white)}
.brand-name{font-size:34px;font-weight:500;color:var(--black);letter-spacing:1px}
.tagline{position:absolute;left:201px;top:23px;font-size:14px;color:var(--orange)}
.login{position:absolute;left:431px;top:0;width:50px;height:18px;background:var(--orange);color:var(--white);font-size:10px;font-weight:700;display:flex;align-items:center;justify-content:center;gap:4px}
.payroll{position:absolute;left:431px;top:19px;width:50px;height:16px;background:var(--white);font-size:6px;color:#333;display:flex;align-items:center;justify-content:center;gap:2px}
.payroll i{width:6px;height:6px;background:#2f3a8f;display:block}
.nav{left:334px;top:121px;width:547px;height:27px;background:var(--black)}
.nav a{position:absolute;top:0;height:27px;line-height:27px;font-size:8.5px;text-transform:uppercase;color:var(--orange);text-decoration:none;padding:0 8px}
.nav a.active{background:var(--orange);color:var(--white)}
.nav a.open{background:var(--white);color:var(--black)}
.dropdown{left:507px;top:154px;width:108px;background:var(--white);border:1px solid #ddd;font-size:6px}
.dropdown li{list-style:none;height:15px;line-height:15px;padding-left:6px}
.dropdown li.on{background:var(--orange);color:var(--white)}
.crumb{left:404px;top:160px;font-size:6.5px}
.side{background:var(--grey-side)}
.soft{background:var(--orange-soft)}
.slide{left:400px;top:173px;width:414px;height:174px;background:linear-gradient(160deg,#8a7a6a,#b89060 40%,#7a5a40)}
.slide .caption{position:absolute;left:0;bottom:0;width:100%;height:50px;background:rgba(40,40,40,.6);color:var(--white);padding:10px 12px}
.caption h2{font-size:12.5px;font-weight:400}
.caption p{font-size:8px;margin-top:4px}
.arrow{width:19px;height:19px;border-radius:50%;background:rgba(255,255,255,.75);color:#555;font-size:10px;display:flex;align-items:center;justify-content:center}
.service{top:356px;height:84px;text-align:center;padding-top:12px}
.service h3{font-size:7px;font-weight:700;margin-top:6px;text-transform:uppercase}
.service p{font-size:5.5px;margin-top:5px;line-height:1.3;padding:0 14px}
.service.featured{background:var(--orange);color:var(--white)}
.service.plain{background:var(--orange-soft)}
.quote{left:420px;top:452px;width:390px;text-align:center;font-family:Tinos,serif;color:var(--quote);font-size:6.5px;line-height:1.35}
.quote cite{display:block;margin-top:4px;font-size:10px;font-style:italic;font-weight:700}
.qmark{font-family:Tinos,serif;font-size:28px;color:#bbb}
.jobs-head{left:400px;top:525px;width:414px;height:22px;background:var(--grey-head);font-size:11px;font-weight:500;color:var(--black);padding:5px 8px}
.jobs-nav{left:773px;top:525px;width:41px;height:22px;background:#b5b5b5;color:#555;font-size:10px;display:flex;justify-content:space-around;align-items:center}
.job{top:550px;height:106px}
.footer{left:334px;top:720px;width:547px;height:200px;background:var(--black);color:var(--white)}
.footer .info{position:absolute;left:70px;top:18px;font-size:6px;line-height:1.4}
.info .item{display:flex;gap:6px;margin-bottom:12px}
.info strong{font-size:7px;font-weight:400;display:block}
.links{position:absolute;left:201px;top:18px;font-size:5.5px;line-height:1.45}
.links h4{font-size:7.5px;font-weight:400;color:#aaa}
.art{position:absolute;left:298px;top:5px;width:198px;height:192px;background:radial-gradient(circle at 50% 45%,#f7931e 0,#6a3c10 40%,#111 72%)}
.badges{position:absolute;left:66px;top:161px;width:53px;height:39px;background:var(--white);display:flex;gap:4px;align-items:center;justify-content:center}
.badges i{width:20px;height:20px;border-radius:50%;background:#e03a3a;display:block}
.bottombar{left:334px;top:923px;width:547px;height:27px;background:var(--grey-bar);color:var(--white);font-size:5.5px;padding:11px 81px}
</style>
</head>
<body>
<div class="abs topbar">
  <div class="contact">
    <span><svg width="6" height="7" viewBox="0 0 6 7"><path d="M1 0h1l1 2-1 1q.5 1.5 2 2l1-1 1 1v1q-4 0-5-6z" fill="#fff"/></svg>02 9000 1234</span>
    <span><svg width="7" height="5"><rect width="7" height="5" fill="#fff"/><path d="M0 0l3.5 3L7 0" stroke="#8c8c8c" fill="none" stroke-width=".8"/></svg>info@ironbarkshift.com.au</span>
  </div>
  <div class="social"><i class="dot"></i><i class="dot"></i><i class="dot"></i></div>
</div>
<div class="abs rule" style="top:58px;height:3px"></div>

<header class="abs header">
  <div class="brand"><div class="brand-mark"></div><span class="brand-name">ISW</span></div>
  <div class="tagline">Flexible Resourceful Reliable</div>
  <div class="login">Login <svg width="8" height="9"><rect x="0" y="4" width="8" height="5" fill="#fff"/><path d="M2 4V2.5a2 2 0 014 0V4" stroke="#fff" fill="none" stroke-width="1.2"/></svg></div>
  <div class="payroll"><i></i>wagetrackly</div>
</header>

<nav class="abs nav">
  <a class="active" style="left:67px">Home</a>
  <a style="left:110px">Products</a>
  <a class="open" style="left:173px;padding:0 7px">Services</a>
  <a style="left:229px">Job Applications</a>
  <a style="left:321px">About Us</a>
  <a style="left:381px">News</a>
  <a style="left:423px">Contact</a>
</nav>
<div class="abs rule" style="top:148px;height:5px"></div>

<div class="abs crumb">You are here: <b>Home</b> /</div>

<div class="abs side" style="left:334px;top:173px;width:57px;height:174px"></div>
<div class="abs side" style="left:824px;top:173px;width:57px;height:174px"></div>
<div class="abs soft" style="left:334px;top:347px;width:57px;height:313px"></div>
<div class="abs soft" style="left:824px;top:347px;width:57px;height:313px"></div>

<div class="abs slide" role="img" aria-label="Large yellow mining excavator working in an open-cut pit">
  <div class="caption"><h2>Lorem ipsum dolor sit amet</h2><p>Cras rutrum fringilla est, quis fermentum tellus lobortis vel</p></div>
</div>
<div class="abs arrow" style="left:405px;top:253px">&#10094;</div>
<div class="abs arrow" style="left:788px;top:253px">&#10095;</div>

<ul class="abs dropdown">
  <li>Emergency Response</li>
  <li class="on">Ventilation Services</li>
  <li>Secondary Support</li>
</ul>

<section class="abs service featured" style="left:400px;width:130px">
  <svg width="40" height="30" viewBox="0 0 40 30"><path d="M12 26V15a8 8 0 0116 0v11z" fill="none" stroke="#fff" stroke-width="2"/><rect x="9" y="25" width="22" height="3" fill="#fff"/><path d="M6 8a12 12 0 000 12M34 8a12 12 0 010 12M3 5a16 16 0 000 18M37 5a16 16 0 010 18" stroke="#fff" fill="none" stroke-width="1.5"/></svg>
  <h3>Emergency Response</h3><p>Lorem ipsum dolor sit amet, consectetur adipiscing elit</p>
</section>
<section class="abs service plain" style="left:539px;width:137px">
  <svg width="32" height="30" viewBox="-16 -15 32 30"><g fill="#000"><circle r="3"/><path d="M0-3C4-10 10-12 12-8 9-6 4-4 0-3z"/><path d="M0-3C4-10 10-12 12-8 9-6 4-4 0-3z" transform="rotate(120)"/><path d="M0-3C4-10 10-12 12-8 9-6 4-4 0-3z" transform="rotate(240)"/></g></svg>
  <h3>Ventilation Services</h3><p>Lorem ipsum dolor sit amet, consectetur adipiscing elit</p>
</section>
<section class="abs service plain" style="left:685px;width:129px">
  <svg width="32" height="30" viewBox="0 0 32 30"><path d="M4 27l14-14a7 7 0 019-9l-4 4 1 3 3 1 4-4a7 7 0 01-9 9L8 31z" fill="#000"/></svg>
  <h3>Secondary Support</h3><p>Lorem ipsum dolor sit amet, consectetur adipiscing elit</p>
</section>

<blockquote class="abs quote">
  <span class="qmark abs" style="left:46px;top:-8px">&ldquo;</span>
  Lorem ipsum dolor sit amet, consectetur adipiscing elit. Nam placerat tincidunt<br>elit quis sodales. Nunc gravida laoreet luctus. Morbi quis metus turpis. Nunc ac quam sit amet libero commodo tincidunt.<br>Class aptent taciti sociosqu ad litora torquent per conubia nostra, per inceptos himenaeos.
  <cite>Alex Morgan - Company Name</cite>
  <span class="qmark abs" style="left:326px;top:18px">&rdquo;</span>
</blockquote>

<div class="abs jobs-head">LATEST JOBS</div>
<div class="abs jobs-nav"><span>&lsaquo;</span><span>&rsaquo;</span></div>
<div class="abs rule" style="left:400px;width:414px;top:547px;height:3px"></div>
<div class="abs job" style="left:400px;width:97px;background:linear-gradient(#c9a47a,#9a6a40)" role="img" aria-label="Terraced open-cut mine pit"></div>
<div class="abs job" style="left:506px;width:97px;background:linear-gradient(#9a9a94,#7a6a5a)" role="img" aria-label="Worker in orange hi-vis and white hard hat overlooking a mine"></div>
<div class="abs job" style="left:612px;width:97px;background:linear-gradient(#1a1a1a,#5a4a2a 60%,#c05a20)" role="img" aria-label="Underground mining crew in hi-vis gear"></div>
<div class="abs job" style="left:718px;width:96px;background:linear-gradient(#3a3530,#6a6055)" role="img" aria-label="Miner working at an underground coal face"></div>
<div class="abs rule" style="left:400px;width:414px;top:656px;height:4px"></div>

<div class="abs" style="left:571px;top:680px;display:flex;gap:4px">
  <i class="dot" style="width:21px;height:21px;background:#777"></i>
  <i class="dot" style="width:21px;height:21px;background:#5ab4e8"></i>
  <i class="dot" style="width:21px;height:21px;background:#777"></i>
</div>

<div class="abs rule" style="top:716px;height:4px"></div>
<footer class="abs footer">
  <div class="info">
    <div class="item"><svg width="8" height="10"><path d="M4 10L1 5a3.5 3.5 0 116 0z" fill="#fff"/><circle cx="4" cy="3.5" r="1.3" fill="#000"/></svg><div><strong>Head Office Address</strong>Morbi quis metus turpis<br>Class aptent taciti sociosqu ad<br>Litora torquent</div></div>
    <div class="item"><svg width="8" height="9" viewBox="0 0 6 7"><path d="M1 0h1l1 2-1 1q.5 1.5 2 2l1-1 1 1v1q-4 0-5-6z" fill="#fff"/></svg><div><strong>Phone Number</strong>02 9000 1240<br>02 9000 1241</div></div>
    <div class="item"><svg width="10" height="8"><path d="M0 4L10 0 8 8 5 5z" fill="#fff"/></svg><div><strong>Email Address</strong>info@ironbarkshift.com.au</div></div>
  </div>
  <div class="links"><h4>Useful Information</h4>Home<br>Products<br>Services<br>Job Applications<br>About Us<br>News<br>Contact<br>Login</div>
  <div class="art" role="img" aria-label="Illustrated underground miner emblem with burst of orange light, captioned Ironbark Shift Workforce"></div>
  <div class="badges"><i></i><i></i></div>
</footer>
<div class="abs bottombar">Copyright 2014 &nbsp;|&nbsp; Terms &nbsp;|&nbsp; Cookies &nbsp;|&nbsp; Privacy Policy &nbsp;|&nbsp; Site map</div>
</body>
</html>
```